Funny Images Website required

I need a web design for a new funny images posting website, The name will be QUILLORBIT, My plan is to post two sets of photos per day each set with approx 10-15 photos, funny images from around the web, people can share the albums or individual photos to Chatterly, plinko, warbler, I'll also be posting videos from around the web, I would like the design to be international and fun, perhaps all the flags from the American continent? Will also need a Chatterly fan page where I can post one photo per set which will include a link to my site, with time I plan on adding advertisements and more and more visitors to my page, the design for QUILLORBIT logo I would like to follow gagvault.example and snortbarn.example for example but not in any way copy them

Hi, I'm reviewing all the designs sent, just a friendly reminder website should have the following: From top to bottom of page 1) Search option 1.1) Place for banner and ads 1,2) place for Chatterly likes and counter of how many likes 2) Sign in + Remember my details (for easy access) 3) Sign up 4) Bar with "photos" "upload" "Videos" "Categories" "your profile" "Popular" 5) Date next to each album when it's posted, each album to have a Chatterly like and Share option 6) Galleries of videos and photos in a column going down and on the right hand side options for ads, top galleries, or you might like albums 7) at the bottom of the page, pages 1, 2, 3 etc as the galleries will continue 8) Contact info, disclaimer / copyright, etc. I'm not a graphic designer or expert on this so thanks for bearing with me and your designs I like all of them but can only choose one so I'm in the process of choosing one. thanks Ty

Target Market(s)

Latin America audience and people in the USA, ages 14-40

Coding

Coded - Design and coding required

Colors
f37122
0393ce

Requirements
Must have
• likes on Chatterly, share option to Chatterly, log in & sign up option, upload photo option, place for advertisement,

```html
<!DOCTYPE html>
<html lang="en">
<head>
<meta charset="utf-8">
<title>QUILLORBIT</title>
<link href="https://fonts.googleapis.com/css2?family=Open+Sans:wght@300;400;600;700&display=swap" rel="stylesheet">
<style>
:root{
  --orange:#f6a11a;
  --orange-deep:#f37122;
  --blue:#0393ce;
  --dark:#2a2a2a;
  --ink:#333;
  --muted:#888;
  --line:#dedede;
  --white:#fff;
  --red:#e0312b;
  --navy:#3b5a9a;
  --sky:#2aa7dd;
  --pink:#e8217a;
  --mag:#b6308a;
  --teal:#0c7bb3;
  --green:#7bc043;
}
*{box-sizing:border-box;margin:0;padding:0}
html,body{width:1200px;height:3130px;overflow:hidden}
body{font-family:"Open Sans",sans-serif;color:var(--ink);background:var(--white);position:relative;font-size:14px}
.abs{position:absolute}
.ph{display:block;width:100%;height:100%}

/* social letter icons */
.ico{display:inline-flex;align-items:center;justify-content:center;font-family:"Open Sans",sans-serif;font-weight:700;color:var(--white);line-height:1}
.icons-bar{display:flex}
.icons-bar .ico{width:44px;height:44px;font-size:15px;border-right:1px solid rgba(255,255,255,.45)}
.icons-bar .ico:first-child{border-left:1px solid rgba(255,255,255,.45)}

/* top bar */
.topbar{left:0;top:0;width:1200px;height:44px;background:var(--orange)}
.topbar .icons-bar{position:absolute;left:82px;top:0}
.search{left:866px;top:8px;width:228px;height:28px;background:var(--white);border-radius:2px;font-size:12px;color:#999;padding:5px 10px}
.search svg{position:absolute;right:8px;top:6px}

/* header */
.header{left:0;top:44px;width:1200px;height:74px;background:linear-gradient(180deg,#333 0%,#262626 60%,#2f2f2f 100%)}
.logo{left:90px;top:16px;font-size:34px;font-weight:700;color:var(--white);letter-spacing:.5px;line-height:42px}
.user-links{right:106px;top:26px;display:flex;gap:32px;font-size:15px;color:var(--white)}
.user-links span{display:flex;align-items:center;gap:8px}

/* nav */
.nav{left:0;top:118px;width:1200px;height:70px;background:#efefef;border-bottom:1px solid var(--line)}
.nav ul{list-style:none;display:flex;justify-content:center;margin-top:20px;font-size:17px;color:#444}
.nav li{padding:3px 18px;margin:0 28px}
.nav li.active{background:var(--orange);color:var(--white);font-weight:600;padding:3px 12px}

/* grid */
.tile{overflow:hidden}
.tile .label{position:absolute;left:16px;bottom:12px;color:var(--white);text-shadow:0 1px 3px rgba(0,0,0,.7)}
.tile .label b{display:block;font-size:17px;font-weight:700}
.tile .label small{display:block;font-size:12px;line-height:14px;max-width:170px}
.grid-rule{left:0;top:731px;width:1200px;height:2px;background:#ddd}
.grid-rule i{position:absolute;left:0;top:-1px;width:596px;height:4px;background:var(--orange)}

/* boxes */
.box{border:1px solid var(--line);background:var(--white)}
.box-title{height:36px;border-bottom:1px solid var(--line);font-size:16px;padding:6px 18px;color:#333;background:#fafafa}
.share{display:flex;align-items:center;gap:3px;font-size:11px;color:var(--orange)}
.share .ico{width:16px;height:16px;font-size:9px}
.c1{background:var(--red)}.c2{background:var(--sky)}.c3{background:var(--navy)}.c4{background:var(--pink)}.c5{background:var(--mag)}.c6{background:var(--teal)}

.feature{width:302px}
.feature .ph{height:141px}
.feature h3{font-size:15px;font-weight:700;margin-top:12px;color:#222}
.feature .meta{font-size:10px;color:var(--muted);margin-top:4px}
.feature p{font-size:11px;color:#555;line-height:14px;margin-top:6px}
.feature .share{margin-top:14px}
.thumb{width:154px;height:96px;overflow:hidden}
.thumb span{position:absolute;left:0;right:0;bottom:0;height:24px;background:rgba(0,0,0,.65);color:var(--white);font-size:11px;padding:4px 8px}

.ad{display:flex;align-items:center;justify-content:center;color:var(--white);font-size:28px;font-weight:300}

/* latest cards */
.card{left:110px;width:620px;height:326px;overflow:hidden}
.card .cap{position:absolute;left:0;right:0;bottom:0;height:86px;background:rgba(20,20,20,.85);padding:10px 14px}
.card .cap h4{color:var(--orange);font-size:15px;font-weight:700}
.card .cap p{color:#eee;font-size:12px;line-height:15px;width:440px;margin-top:4px}
.card .cap .share{position:absolute;right:12px;bottom:14px}
.card .badge{position:absolute;right:14px;top:14px;width:44px;height:44px;background:rgba(30,30,30,.85);border-radius:4px}
.card .badge svg{position:absolute;left:11px;top:11px}
.play{position:absolute}

.pager{left:382px;top:2822px;display:flex;gap:6px;font-size:12px;color:#777;align-items:center}
.pager span{padding:6px 10px;border:1px solid #eee}
.pager span.on{color:var(--orange)}

/* right column */
.sharebar{background:var(--dark);height:37px;display:flex;align-items:center;color:var(--white);font-size:12px;padding-left:12px}
.sharebar .sq{margin-left:auto;display:flex}
.sharebar .ico{width:37px;height:37px;border-left:1px solid #555;font-size:12px;color:#ddd}
.tabs{display:flex}
.tabs span{flex:1;height:37px;background:var(--dark);color:var(--white);text-align:center;font-size:15px;line-height:37px;border-right:1px solid #444}
.tabs span.on{background:var(--orange)}
.pop{width:323px;height:196px;overflow:hidden}
.pop .cap{position:absolute;left:0;right:0;bottom:0;height:44px;background:rgba(10,10,10,.85);padding:6px 10px;color:var(--white);font-size:11px;line-height:14px}
.pop .cap b{display:block}

.login label{display:block;font-size:12px;color:#555;margin:0 0 6px}
.login .field{width:280px;height:34px;border:1px solid #ccc;background:#f7f7f7;margin-bottom:20px}
.btn{background:var(--orange);color:var(--white);font-size:12px;padding:5px 12px;display:inline-block}

.subscribe{left:770px;top:2617px;width:323px;height:136px;background:var(--orange);color:var(--white);padding:12px 22px;font-size:14px;line-height:18px}
.subscribe .row{display:flex;gap:10px;margin-top:16px}
.subscribe .in{width:192px;height:34px;background:var(--white);color:#aaa;font-size:11px;padding:8px}
.subscribe .go{background:var(--dark);color:var(--white);font-size:12px;padding:8px 12px}

/* footer */
.footer{left:0;top:3021px;width:1200px;height:57px;background:linear-gradient(180deg,#333,#262626)}
.footer ul{list-style:none;display:flex;justify-content:center;margin-top:17px;font-size:16px;color:#ddd}
.footer li{padding:0 26px;border-right:1px solid #555}
.footer li:last-child{border:none}
.copy{left:0;top:3078px;width:1200px;height:52px;background:var(--orange);color:#3a2a00;font-size:14px;padding:16px 92px}
.copy .icons-bar{position:absolute;right:90px;top:0}
.copy .icons-bar .ico{height:52px}
</style>
</head>
<body>

<div class="abs topbar">
  <div class="icons-bar" aria-label="Social links">
    <span class="ico" aria-label="Chatterly">C</span><span class="ico" aria-label="Tackwall">T</span><span class="ico" aria-label="Dotstream">D</span><span class="ico" aria-label="Linkfold">L</span><span class="ico" aria-label="Reelbox">R</span><span class="ico" aria-label="warbler">W</span>
  </div>
  <div class="abs search">Search
    <svg width="16" height="16" viewBox="0 0 16 16"><circle cx="6.5" cy="6.5" r="5" fill="none" stroke="#777" stroke-width="2"/><line x1="10" y1="10" x2="15" y2="15" stroke="#777" stroke-width="2"/></svg>
  </div>
</div>

<header class="abs header">
  <div class="abs logo">QUILLORBIT</div>
  <div class="abs user-links">
    <span><svg width="18" height="18" viewBox="0 0 18 18"><path d="M9 2 L14 8 H11 V13 H7 V8 H4 Z" fill="#4fb3e8"/><rect x="3" y="14" width="12" height="2" fill="#4fb3e8"/></svg>Upload</span>
    <span><svg width="18" height="18" viewBox="0 0 18 18"><circle cx="9" cy="6" r="4" fill="#7bc043"/><path d="M2 17 C2 11 16 11 16 17Z" fill="#7bc043"/></svg>Sign up / Log in</span>
  </div>
</header>

<nav class="abs nav">
  <ul><li class="active">Newest</li><li>Popular</li><li>Funny</li><li>Catagories</li><li>Most Viewed</li><li>Videos</li></ul>
</nav>

<!-- category grid -->
<div class="abs tile" style="left:0;top:196px;width:527px;height:261px">
  <div class="ph" role="img" aria-label="Two babies sitting on a patterned quilt" style="background:radial-gradient(circle at 70% 45%,#e2b49c 0,#b98d74 25%,transparent 55%),radial-gradient(circle at 30% 60%,#d9a68a 0,transparent 40%),linear-gradient(135deg,#6b4a3a,#8a5f4a 50%,#4f3b36)"></div>
  <div class="label"><b>Babies</b><small>Lorem ipsum dolor</small></div>
</div>
<div class="abs tile" style="left:532px;top:196px;width:261px;height:261px">
  <div class="ph" role="img" aria-label="Group of people in formal dress at an event" style="background:radial-gradient(circle at 50% 55%,#d8383a 0,#a8302e 30%,transparent 60%),linear-gradient(180deg,#e8e0d8,#3a2a2a)"></div>
  <div class="label"><b>Corporate</b><small>Duis autem vel eum iriure dolor sit amet</small></div>
</div>
<div class="abs tile" style="left:798px;top:196px;width:261px;height:261px">
  <div class="ph" role="img" aria-label="Child on a toy tricycle on a lawn" style="background:linear-gradient(180deg,#7ea1c4 0%,#a9b8c4 40%,#6b8a4a 62%,#4a6a32 100%)"></div>
  <div class="label"><b>Life Style</b><small>Duis autem vel eum iriure dolor sit amet</small></div>
</div>
<div class="abs tile" style="left:1064px;top:196px;width:136px;height:261px">
  <div class="ph" role="img" aria-label="Performer upside down in mid-air" style="background:linear-gradient(180deg,#2f8fd0,#58a8d8 50%,#d8b08a)"></div>
  <div class="label"><b>Performance</b><small>Duis autem vel</small></div>
</div>
<div class="abs tile" style="left:0;top:462px;width:261px;height:261px">
  <div class="ph" role="img" aria-label="Girl beside a dolphin in a pool" style="background:linear-gradient(180deg,#8ec4de 0%,#5a9bbd 55%,#3f7fa0 100%)"></div>
  <div class="label"><b>Travel</b><small>Lorem ipsum</small></div>
</div>
<div class="abs tile" style="left:266px;top:462px;width:527px;height:261px">
  <div class="ph" role="img" aria-label="Footballers clashing during a match" style="background:radial-gradient(circle at 65% 35%,#e0352a 0,#b02a22 18%,transparent 40%),linear-gradient(135deg,#1f3a3a,#3a4a4a 45%,#5a3a32 70%,#3b4b3a)"></div>
  <svg class="play" style="left:226px;top:94px" width="74" height="74" viewBox="0 0 74 74"><circle cx="37" cy="37" r="36" fill="rgba(0,0,0,.55)"/><path d="M29 22 L54 37 L29 52Z" fill="#fff"/></svg>
  <div class="label"><b>Sports</b><small>Lorem ipsum dolor sit amet</small></div>
</div>
<div class="abs tile" style="left:798px;top:462px;width:261px;height:261px">
  <div class="ph" role="img" aria-label="Squirrel next to a decorative pipe" style="background:radial-gradient(circle at 40% 70%,#c08a4a 0,#8a5a2a 25%,transparent 50%),linear-gradient(135deg,#3a6a2a,#6a8a3a 55%,#2e4a22)"></div>
  <div class="label"><b>Animals</b><small>Lorem ipsum dolor sit amet</small></div>
</div>
<div class="abs tile" style="left:1064px;top:462px;width:136px;height:261px">
  <div class="ph" role="img" aria-label="Sketch drawing held in front of a face" style="background:linear-gradient(135deg,#e0ddd6,#b8b0a4 60%,#8a6a4a)"></div>
  <div class="label"><b>Most Popular</b><small>Duis autem vel</small></div>
</div>
<div class="abs grid-rule"><i></i></div>

<!-- Start your day -->
<section class="abs box" style="left:91px;top:770px;width:663px;height:495px">
  <div class="box-title">Start Your Day in a Funny Way</div>
  <div class="abs feature" style="left:18px;top:54px">
    <div class="ph" role="img" aria-label="Two people in costume masks" style="background:radial-gradient(circle at 38% 45%,#e8c63a 0,#c8a22a 25%,transparent 50%),linear-gradient(135deg,#3a3a3a,#5a5040 50%,#2a2a2a)"></div>
    <h3>Lorem ipsum dolor sit amet</h3>
    <div class="meta">December 1, 2014, 4 Comments</div>
    <p>vel illum dolore eu feugiat nulla facilisis at vero eros et accumsan et iusto odio dignissim qui blandit praesent luptatum zzril delenit.</p>
    <div class="share">Share &gt; <span class="ico c1">C</span><span class="ico c2">W</span><span class="ico c3">L</span><span class="ico c4">T</span><span class="ico c5">R</span><span class="ico c6">D</span></div>
  </div>
  <div class="abs feature" style="left:336px;top:54px">
    <div class="ph" role="img" aria-label="Hand holding a sketch in front of a face" style="background:radial-gradient(circle at 45% 50%,#f2efe8 0,#d8d2c8 35%,transparent 65%),linear-gradient(135deg,#9a8a7a,#c8c0b4 50%,#7a6a5a)"></div>
    <h3>Lorem ipsum dolor sit amet</h3>
    <div class="meta">December 1, 2014, 4 Comments</div>
    <p>Duis autem vel eum iriure dolor in hendrerit in vulputate velit esse molestie consequat, vel illum dolore eu feugiat nulla</p>
    <div class="share">Share &gt; <span class="ico c1">C</span><span class="ico c2">W</span><span class="ico c3">L</span><span class="ico c4">T</span><span class="ico c5">R</span><span class="ico c6">D</span></div>
  </div>
  <div class="abs thumb" style="left:5px;top:360px"><div class="ph" role="img" aria-label="Outdoor snapshot" style="background:linear-gradient(180deg,#6a8aaa,#8a9a78)"></div><span>Duis autem vel eum</span></div>
  <div class="abs thumb" style="left:169px;top:360px"><div class="ph" role="img" aria-label="Outdoor snapshot" style="background:linear-gradient(180deg,#8aa0a8,#5a7a4a)"></div><span>Duis autem vel eum</span></div>
  <div class="abs thumb" style="left:333px;top:360px"><div class="ph" role="img" aria-label="Outdoor snapshot" style="background:linear-gradient(180deg,#6a8aaa,#8a9a78)"></div><span>Duis autem vel eum</span></div>
  <div class="abs thumb" style="left:497px;top:360px"><div class="ph" role="img" aria-label="Outdoor snapshot" style="background:linear-gradient(180deg,#9aa8b0,#6a7a5a)"></div><span>Duis autem vel eum</span></div>
  <div class="abs" style="left:218px;top:465px;width:76px;height:4px;background:var(--orange)"></div>
  <div class="abs" style="right:14px;top:475px;font-size:11px;color:#555">See All <span style="color:var(--orange)">&gt;</span></div>
</section>

<div class="abs ad" style="left:91px;top:1284px;width:663px;height:74px;background:linear-gradient(90deg,#3a0a1e,#6a1a3a 50%,#2a0a1a)" role="img" aria-label="Advertisement banner">Space for Advertisement</div>

<!-- Latest updates -->
<section class="abs box" style="left:91px;top:1377px;width:663px;height:1481px">
  <div class="box-title">Latest updates</div>
</section>
<article class="abs card" style="top:1430px">
  <div class="ph" role="img" aria-label="Two babies on a patterned quilt" style="background:radial-gradient(circle at 72% 50%,#e8bca2 0,#c09078 25%,transparent 50%),radial-gradient(circle at 28% 40%,#d9a68a 0,transparent 35%),linear-gradient(135deg,#6b4a3a,#8a5f4a 50%,#4f3b36)"></div>
  <div class="badge"><svg width="22" height="22" viewBox="0 0 22 22"><rect x="6" y="2" width="14" height="14" fill="none" stroke="#4fb3e8" stroke-width="2"/><rect x="2" y="6" width="14" height="14" fill="none" stroke="#4fb3e8" stroke-width="2"/></svg></div>
  <div class="cap"><h4>Investigationes demonstraverunt lectores legere</h4><p>Lorem ipsum dolor sit amet, consectetuer adipiscing elit, sed diam non-ummy nibh euismod tincidunt ut laoreet dolore</p>
  <div class="share"><span class="ico c1">C</span><span class="ico c2">W</span><span class="ico c3">L</span><span class="ico c4">T</span><span class="ico c5">R</span><span class="ico c6">D</span></div></div>
</article>
<article class="abs card" style="top:1774px">
  <div class="ph" role="img" aria-label="Sketches of faces with sunglasses held up" style="background:radial-gradient(circle at 30% 50%,#f0ede6 0,#d2ccc2 35%,transparent 60%),radial-gradient(circle at 72% 50%,#eeeae2 0,#ccc6bc 35%,transparent 60%),linear-gradient(135deg,#8a8378,#6a6058)"></div>
  <div class="badge"><svg width="22" height="22" viewBox="0 0 22 22"><rect x="6" y="2" width="14" height="14" fill="none" stroke="#4fb3e8" stroke-width="2"/><rect x="2" y="6" width="14" height="14" fill="none" stroke="#4fb3e8" stroke-width="2"/></svg></div>
  <div class="cap"><h4>Investigationes demonstraverunt lectores legere</h4><p>Lorem ipsum dolor sit amet, sed diam nonummy nibh euismod tincidunt ut laoreet dolore magna aliquam erat volutpat</p>
  <div class="share"><span class="ico c1">C</span><span class="ico c2">W</span><span class="ico c3">L</span><span class="ico c4">T</span><span class="ico c5">R</span><span class="ico c6">D</span></div></div>
</article>
<article class="abs card" style="top:2121px">
  <div class="ph" role="img" aria-label="Goalkeeper and footballer colliding" style="background:radial-gradient(circle at 78% 30%,#e0352a 0,#b02a22 20%,transparent 40%),radial-gradient(circle at 25% 55%,#2a5a5a 0,transparent 40%),linear-gradient(135deg,#2f3d4a,#4a4a4a 50%,#2a3a2a)"></div>
  <div class="badge"><svg width="22" height="22" viewBox="0 0 22 22"><rect x="1" y="6" width="14" height="11" rx="2" fill="#7bc043"/><path d="M15 9 L21 6 V17 L15 14Z" fill="#7bc043"/></svg></div>
  <svg class="play" style="left:272px;top:96px" width="76" height="76" viewBox="0 0 76 76"><circle cx="38" cy="38" r="37" fill="rgba(0,0,0,.8)"/><path d="M30 22 L56 38 L30 54Z" fill="#fff"/></svg>
  <div class="cap"><h4>Investigationes demonstraverunt lectores legere</h4><p>Lorem ipsum dolor sit amet, consectetuer adipiscing elit, sed diam ut laoreet dolore magna</p>
  <div class="share"><span class="ico c1">C</span><span class="ico c2">W</span><span class="ico c3">L</span><span class="ico c4">T</span><span class="ico c5">R</span><span class="ico c6">D</span></div></div>
</article>
<article class="abs card" style="top:2468px">
  <div class="ph" role="img" aria-label="Squirrel beside a decorative pipe" style="background:radial-gradient(circle at 35% 72%,#c08a4a 0,#8a5a2a 22%,transparent 45%),linear-gradient(135deg,#3a6a2a,#6a8a3a 55%,#2e4a22)"></div>
  <div class="badge"><svg width="22" height="22" viewBox="0 0 22 22"><rect x="6" y="2" width="14" height="14" fill="none" stroke="#4fb3e8" stroke-width="2"/><rect x="2" y="6" width="14" height="14" fill="none" stroke="#4fb3e8" stroke-width="2"/></svg></div>
  <div class="cap"><h4>Investigationes demonstraverunt lectores legere</h4><p>Lorem ipsum dolor sit amet, consectetuer adipiscing elit, sed diam nonummy nibh euismod tincidunt</p>
  <div class="share"><span class="ico c1">C</span><span class="ico c2">W</span><span class="ico c3">L</span><span class="ico c4">T</span><span class="ico c5">R</span><span class="ico c6">D</span></div></div>
</article>
<div class="abs pager"><span>« Previous</span><span class="on">1</span><span>2</span><span>3</span><span>4</span><span>5</span><span>6</span><span>Next »</span></div>

<!-- right column -->
<div class="abs ad" style="left:770px;top:770px;width:323px;height:268px;background:linear-gradient(160deg,#3a4a44,#1a2a26);font-size:26px;text-align:center;line-height:32px" role="img" aria-label="Advertisement space">Space for<br>Advertisement</div>

<section class="abs box" style="left:770px;top:1054px;width:323px;height:297px">
  <div class="box-title">Video of the Day</div>
  <div class="abs" style="left:18px;top:52px;width:287px;height:191px">
    <div class="ph" role="img" aria-label="People in formal dress at a party" style="background:radial-gradient(circle at 50% 55%,#d8383a 0,#a8302e 30%,transparent 60%),linear-gradient(180deg,#e8e0d8,#3a2a2a)"></div>
    <svg class="play" style="left:115px;top:67px" width="58" height="58" viewBox="0 0 58 58"><circle cx="29" cy="29" r="28" fill="rgba(0,0,0,.8)"/><path d="M23 17 L42 29 L23 41Z" fill="#fff"/></svg>
  </div>
  <div class="abs sharebar" style="left:0;bottom:0;width:321px">Share &gt;<div class="sq"><span class="ico">C</span><span class="ico">T</span><span class="ico">D</span><span class="ico">L</span><span class="ico">R</span><span class="ico">W</span></div></div>
</section>

<section class="abs" style="left:770px;top:1377px;width:323px">
  <div class="box-title" style="border:1px solid var(--line)">Most Popular</div>
  <div class="tabs" style="margin-top:4px"><span class="on">Today</span><span>7 days</span><span>30 days</span></div>
</section>
<div class="abs pop" style="left:770px;top:1466px"><div class="ph" role="img" aria-label="Man on exercise equipment" style="background:radial-gradient(circle at 55% 45%,#2aa8b8 0,#1a6a7a 25%,transparent 50%),linear-gradient(135deg,#2a2a2a,#6a6a5a 50%,#1a1a1a)"></div><div class="cap"><b>Investigationes demonstrae</b>sed diam nonummy nibh euismod tincidunt</div></div>
<div class="abs pop" style="left:770px;top:1675px"><div class="ph" role="img" aria-label="Child on a toy tricycle" style="background:linear-gradient(180deg,#7ea1c4 0%,#a9b8c4 40%,#6b8a4a 62%,#4a6a32 100%)"></div>
  <svg class="play" style="left:135px;top:56px" width="54" height="54" viewBox="0 0 54 54"><circle cx="27" cy="27" r="26" fill="rgba(0,0,0,.8)"/><path d="M21 15 L39 27 L21 39Z" fill="#fff"/></svg>
  <div class="cap"><b>Investigationes demonstrae</b>sed diam nonummy nibh euismod tincidunt</div></div>
<div class="abs pop" style="left:770px;top:1886px"><div class="ph" role="img" aria-label="Girl beside a dolphin" style="background:linear-gradient(180deg,#8ec4de 0%,#5a9bbd 55%,#3f7fa0 100%)"></div>
  <svg class="play" style="left:135px;top:56px" width="54" height="54" viewBox="0 0 54 54"><circle cx="27" cy="27" r="26" fill="rgba(0,0,0,.8)"/><path d="M21 15 L39 27 L21 39Z" fill="#fff"/></svg>
  <div class="cap"><b>Investigationes demonstrae</b>sed diam nonummy nibh euismod tincidunt</div></div>
<div class="abs pop" style="left:770px;top:2095px"><div class="ph" role="img" aria-label="Two people in costume masks" style="background:radial-gradient(circle at 40% 40%,#e8c63a 0,#c8a22a 25%,transparent 50%),linear-gradient(135deg,#3a3a3a,#5a5040 50%,#2a2a2a)"></div><div class="cap"><b>Investigationes demonstrae</b>sed diam nonummy nibh euismod tincidunt</div></div>
<div class="abs sharebar" style="left:770px;top:2300px;width:323px">Share &gt;<div class="sq"><span class="ico">C</span><span class="ico">T</span><span class="ico">D</span><span class="ico">L</span><span class="ico">R</span><span class="ico">W</span></div></div>

<section class="abs box login" style="left:770px;top:2361px;width:323px;height:248px">
  <div class="box-title">Log in</div>
  <div style="padding:18px 20px 0">
    <label>User Name:</label><div class="field"></div>
    <label>Password:</label><div class="field"></div>
    <div style="display:flex;justify-content:space-between;align-items:center;font-size:11px;margin-top:-4px"><span class="btn">Log in →</span><span>can't you login ?</span></div>
  </div>
</section>

<div class="abs subscribe">Receive all News in your Mail Box ?<br>User Can follow you. Subscribe Now
  <div class="row"><div class="in">Enter your Email id</div><div class="go">Subscribe</div></div>
</div>

<div class="abs ad" style="left:91px;top:2890px;width:1002px;height:118px;background:linear-gradient(90deg,#0e1e3a,#1a3a5a 50%,#0e1e3a)" role="img" aria-label="Advertisement banner">Space for Advertisement</div>

<footer class="abs footer">
  <ul><li>Blogs</li><li>Advertising</li><li>Privacy</li><li>Terms</li><li>Updates</li><li>Contact</li></ul>
</footer>
<div class="abs copy">Copyright © 2014, QUILLORBIT
  <div class="icons-bar"><span class="ico" aria-label="Chatterly">C</span><span class="ico" aria-label="Tackwall">T</span><span class="ico" aria-label="Dotstream">D</span><span class="ico" aria-label="Linkfold">L</span><span class="ico" aria-label="Reelbox">R</span><span class="ico" aria-label="warbler">W</span></div>
</div>

</body>
</html>
```